Business cards and letterhead
Business cards and letterhead - Pharmacy/Pharmaceuticals
Creative Brief
Professional
Owen Lilcroft
Partner
4178 Heron Lake Road Suite 410 Grapevine, TX 76099
owen@torvalepz.com
torvalepz.com

```html
<!DOCTYPE html>
<html lang="en">
<head>
<meta charset="utf-8">
<title>Torvale Business Cards</title>
<link href="https://fonts.googleapis.com/css2?family=Open+Sans:wght@400;600;800&display=swap" rel="stylesheet">
<style>
  :root {
    --page-bg: #e6e8eb;
    --card-white: #ffffff;
    --brand-blue: #1f6fc4;
    --brand-deep: #114a93;
    --band-light: #5d9be0;
    --band-dark: #1a5bb4;
    --text-on-band: #ffffff;
    --shadow: rgba(20, 30, 50, 0.18);
  }
  * { margin: 0; padding: 0; box-sizing: border-box; }
  html, body {
    width: 1200px; height: 770px; overflow: hidden;
    background: var(--page-bg);
    font-family: "Open Sans", Arial, sans-serif;
  }
  .sheet {
    width: 1200px; height: 770px;
    display: flex; align-items: center; justify-content: center; gap: 60px;
  }
  .card {
    position: relative;
    width: 540px; height: 310px;
    background: var(--card-white);
    border-radius: 14px;
    box-shadow: 0 10px 30px var(--shadow);
    overflow: hidden;
  }
  .brand {
    display: flex; align-items: center; gap: 12px;
  }
  .brand-mark {
    width: 46px; height: 46px; border-radius: 50%;
    background: var(--brand-blue);
  }
  .brand-name {
    font-weight: 800; font-size: 42px; color: var(--brand-blue);
    letter-spacing: -0.5px; line-height: 1;
  }
  .card-front .brand {
    position: absolute; left: 50%; top: 50%;
    transform: translate(-50%, -50%);
  }
  .card-back .brand {
    position: absolute; left: 50%; top: 44px;
    transform: translateX(-50%);
  }
  .card-back .brand-mark { width: 40px; height: 40px; }
  .card-back .brand-name { font-size: 36px; }
  .band {
    position: absolute; left: 0; bottom: 0;
    width: 540px; height: 200px;
  }
  .contact {
    position: absolute; left: 0; right: 0; bottom: 34px;
    display: flex; justify-content: center; gap: 22px;
    color: var(--text-on-band);
  }
  .contact-person {
    text-align: right; width: 220px;
    padding-right: 22px;
    border-right: 1px solid rgba(255,255,255,0.6);
  }
  .person-name { font-size: 15px; font-weight: 600; }
  .person-role { font-size: 11px; margin-bottom: 14px; }
  .person-address { font-size: 10.5px; line-height: 1.5; }
  .contact-lines { list-style: none; width: 200px; }
  .contact-lines li {
    display: flex; align-items: center; gap: 8px;
    font-size: 11px; line-height: 1; margin-bottom: 7px;
  }
  .contact-lines svg { width: 13px; height: 13px; flex: none; }
  .contact-lines .gap { margin-top: 6px; }
</style>
</head>
<body>
<main class="sheet">
  <section class="card card-front">
    <div class="brand">
      <span class="brand-mark"></span>
      <span class="brand-name">Torvale</span>
    </div>
  </section>

  <section class="card card-back">
    <div class="brand">
      <span class="brand-mark"></span>
      <span class="brand-name">Torvale</span>
    </div>
    <svg class="band" viewBox="0 0 540 200" preserveAspectRatio="none" aria-hidden="true">
      <defs>
        <linearGradient id="bandFill" x1="0" y1="0" x2="0" y2="1">
          <stop offset="0" stop-color="var(--band-light)"/>
          <stop offset="1" stop-color="var(--band-dark)"/>
        </linearGradient>
      </defs>
      <path d="M0 40 Q270 -10 540 30 L540 200 L0 200 Z" fill="url(#bandFill)"/>
      <path d="M0 52 Q270 4 540 44" fill="none" stroke="#ffffff" stroke-width="3" opacity="0.85"/>
    </svg>
    <div class="contact">
      <div class="contact-person">
        <p class="person-name">Owen Lilcroft</p>
        <p class="person-role">Partner</p>
        <p class="person-address">4178 Heron Lake Road Suite 410<br>Grapevine, TX 76099</p>
      </div>
      <ul class="contact-lines">
        <li><svg viewBox="0 0 14 14"><circle cx="7" cy="7" r="7" fill="#fff"/><path d="M4.5 3.5l1.6 0 .6 2-1 .8a5 5 0 0 0 2.5 2.5l.8-1 2 .6v1.6c-3.8.4-6.9-2.7-6.5-6.5z" fill="var(--brand-blue)"/></svg>214-555-0147</li>
        <li><svg viewBox="0 0 14 14"><circle cx="7" cy="7" r="7" fill="#fff"/><rect x="4" y="4" width="6" height="6" rx="1" fill="var(--brand-blue)"/></svg>214-555-0182</li>
        <li><svg viewBox="0 0 14 14"><circle cx="7" cy="7" r="7" fill="#fff"/><path d="M4.5 3.5l1.6 0 .6 2-1 .8a5 5 0 0 0 2.5 2.5l.8-1 2 .6v1.6c-3.8.4-6.9-2.7-6.5-6.5z" fill="var(--brand-blue)"/></svg>214-555-0163</li>
        <li class="gap"><svg viewBox="0 0 14 14"><circle cx="7" cy="7" r="7" fill="#fff"/><rect x="3.5" y="4.5" width="7" height="5" fill="none" stroke="var(--brand-blue)"/><path d="M3.5 4.5l3.5 3 3.5-3" fill="none" stroke="var(--brand-blue)"/></svg>owen@torvalepz.com</li>
        <li><svg viewBox="0 0 14 14"><circle cx="7" cy="7" r="7" fill="#fff"/><circle cx="7" cy="7" r="3.5" fill="none" stroke="var(--brand-blue)"/><path d="M3.5 7h7M7 3.5v7" stroke="var(--brand-blue)"/></svg>torvalepz.com</li>
      </ul>
    </div>
  </section>
</main>
</body>
</html>
```